Meridale Vantage Alliance Web Design

I would like a web design for a conference. Registration, Form completion, Hotel, Speakers etc. See link for sample similar but not the same.
http://qrvlo.example/pldwk/index.php/contact-us
We would like the design to depict the colours of the logo which is attached. A banner of the website will be provided. We would like a transitioning space in the top and front page of the website for announcements and showcase of events. We would like custom prepared headers for each grouping, example, Sponsor, Venue, Discussion etc.

Hotel

Coded - Design and coding required

```html
<!DOCTYPE html>
<html lang="en">
<head>
<meta charset="utf-8">
<title>Meridale Vantage Alliance Conference 2015</title>
<link rel="stylesheet" href="https://fonts.googleapis.com/css2?family=Lato:wght@300;400;700&family=Merriweather:wght@300;400&display=swap">
<style>
  :root {
    --topbar: #34506f;
    --header-top: #6d8fb4;
    --header-bottom: #4d73a0;
    --page-bg: #ebebeb;
    --panel: #ffffff;
    --nav-bg: #f4f4f4;
    --nav-line: #dcdcdc;
    --nav-text: #7c7c7c;
    --heading-blue: #3d5a7f;
    --title-text: #444a52;
    --body-text: #666666;
    --caption-bg: rgba(40, 45, 55, 0.86);
    --icon-top: #5f82aa;
    --icon-bottom: #2f4d72;
    --dot: #d6d6d6;
    --dot-active: #9a9a9a;
  }
  * { margin: 0; padding: 0; box-sizing: border-box; }
  html, body { width: 1200px; height: 1021px; overflow: hidden; }
  body {
    position: relative;
    background: var(--page-bg);
    font-family: Arial, Helvetica, sans-serif;
  }
  .header-band {
    position: absolute; left: 0; top: 0; width: 1200px; height: 494px;
    background: linear-gradient(180deg, var(--header-top) 0%, var(--header-bottom) 100%);
  }
  .header-band::after {
    content: ""; position: absolute; left: 420px; top: 31px; width: 520px; height: 160px;
    background: radial-gradient(ellipse at 50% 0%, rgba(255,255,255,0.22), rgba(255,255,255,0) 70%);
  }
  .topbar {
    position: absolute; left: 0; top: 0; width: 1200px; height: 31px;
    background: var(--topbar);
  }
  .topbar-links { position: absolute; left: 111px; top: 7px; display: flex; gap: 24px; }
  .topbar-links a { color: #e6edf5; text-decoration: none; font-size: 13px; font-family: Arial, sans-serif; }
  .topbar-links a:nth-child(4) { margin-left: 9px; }
  .social { position: absolute; left: 952px; top: 6px; display: flex; gap: 11px; }
  .social span { width: 16px; height: 16px; border-radius: 2px; display: block; }
  .logo {
    position: absolute; left: 96px; top: 68px; display: flex; align-items: center; gap: 10px;
    color: #ffffff; font-family: Lato, sans-serif; font-weight: 700;
  }
  .logo-mark { width: 58px; height: 58px; border-radius: 50%; border: 5px solid #ffffff; }
  .logo-name { font-size: 17px; line-height: 19px; text-transform: uppercase; }
  .logo-place { font-size: 8px; line-height: 12px; margin-top: 3px; text-transform: uppercase; }
  .contact { position: absolute; right: 107px; top: 79px; text-align: right; color: #ffffff; font-family: Lato, sans-serif; }
  .contact .phone { font-size: 17px; display: flex; align-items: center; justify-content: flex-end; gap: 8px; }
  .contact .mail { font-size: 15px; font-weight: 300; margin-top: 8px; display: flex; align-items: center; justify-content: flex-end; gap: 9px; }
  .page {
    position: absolute; left: 98px; top: 167px; width: 1001px; height: 900px;
    background: var(--panel); box-shadow: 0 0 6px rgba(0,0,0,0.12);
  }
  .page::before {
    content: ""; position: absolute; left: 0; top: 0; width: 100%; height: 11px; background: #4a6789;
  }
  .main-nav {
    position: absolute; left: 0; top: 11px; width: 100%; height: 60px;
    background: var(--nav-bg); border-bottom: 1px solid var(--nav-line);
    display: flex; box-shadow: 0 2px 3px rgba(0,0,0,0.08);
  }
  .main-nav a {
    font-family: Lato, sans-serif; font-weight: 700; font-size: 14px; letter-spacing: 0.4px;
    color: var(--nav-text); text-decoration: none; text-transform: uppercase;
    display: flex; align-items: center; justify-content: center; border-right: 1px solid var(--nav-line);
  }
  .main-nav .search { margin-left: auto; width: 60px; display: flex; align-items: center; justify-content: center; }
  .slider {
    position: absolute; left: 21px; top: 91px; width: 958px; height: 392px;
    background: linear-gradient(100deg, #c9d6e2 0%, #e8eef4 35%, #dfe5ea 60%, #b8c6d4 100%);
  }
  .caption {
    position: absolute; left: 20px; top: 236px; width: 478px; height: 137px;
    background: var(--caption-bg); color: #ffffff; padding: 26px 27px;
  }
  .caption h2 { font-family: Lato, sans-serif; font-weight: 300; font-size: 25px; letter-spacing: 0.2px; }
  .caption p { font-family: Merriweather, serif; font-weight: 300; font-size: 13px; line-height: 21px; margin-top: 12px; color: #e8e8e8; }
  .slider-arrows {
    position: absolute; left: 500px; top: 341px; width: 67px; height: 32px;
    background: rgba(40,45,55,0.92); display: flex; align-items: center; justify-content: center; gap: 16px;
  }
  .dots { position: absolute; left: 927px; top: 504px; display: flex; gap: 8px; }
  .dots span { width: 8px; height: 8px; border-radius: 50%; background: var(--dot); }
  .dots span.active { background: var(--dot-active); }
  .section-title {
    position: absolute; left: 22px; top: 530px; width: 958px; padding-bottom: 10px;
    border-bottom: 1px solid #e2e2e2;
    font-family: Lato, sans-serif; font-weight: 400; font-size: 27px; color: var(--heading-blue);
  }
  .features { position: absolute; left: 22px; top: 617px; width: 960px; display: grid; grid-template-columns: 327px 327px 300px; row-gap: 32px; }
  .feature-head { display: flex; align-items: center; gap: 11px; }
  .feature-icon {
    width: 37px; height: 37px; border-radius: 50%;
    background: linear-gradient(180deg, var(--icon-top), var(--icon-bottom));
    display: flex; align-items: center; justify-content: center;
  }
  .feature-head h3 { font-family: Lato, sans-serif; font-weight: 400; font-size: 20px; color: var(--title-text); }
  .feature p { font-size: 13px; line-height: 20px; color: var(--body-text); margin-top: 12px; width: 300px; }
</style>
</head>
<body>
  <div class="header-band"></div>
  <div class="topbar">
    <nav class="topbar-links">
      <a href="#">Home</a><a href="#">Support</a><a href="#">About</a><a href="#">Contact</a>
    </nav>
    <div class="social">
      <span style="background:#5a6a60"></span><span style="background:#d9362c"></span><span style="background:#1f72b4"></span><span style="background:#72b83a"></span><span style="background:#3f5c80"></span><span style="background:#3aa7de"></span>
    </div>
  </div>

  <div class="logo">
    <div class="logo-mark"></div>
    <div>
      <div class="logo-name">Meridale Vantage<br>Alliance Conference 2015</div>
      <div class="logo-place">Harlow Point, Vessen Isles</div>
    </div>
  </div>

  <div class="contact">
    <div class="phone">
      <svg width="9" height="13" viewBox="0 0 9 13"><rect x="0.5" y="0.5" width="8" height="12" rx="1.5" fill="none" stroke="#fff"/><rect x="2" y="2.5" width="5" height="6" fill="#fff"/></svg>
      Call Us : 0000-0000-0000
    </div>
    <div class="mail">
      <svg width="12" height="9" viewBox="0 0 12 9"><rect width="12" height="9" fill="#fff"/><path d="M0 0 L6 5 L12 0" fill="none" stroke="#5a7ca5"/></svg>
      your@domain.com
    </div>
  </div>

  <main class="page">
    <nav class="main-nav">
      <a href="#" style="width:107px">Home</a>
      <a href="#" style="width:116px">About Us</a>
      <a href="#" style="width:127px">Services</a>
      <a href="#" style="width:101px">Blog</a>
      <a href="#" style="width:122px">Gallery</a>
      <a href="#" style="width:157px">Presentation</a>
      <a href="#" style="width:153px">Contact Us</a>
      <span class="search">
        <svg width="16" height="16" viewBox="0 0 16 16"><circle cx="6.5" cy="6.5" r="5" fill="none" stroke="#8a8a8a" stroke-width="2"/><line x1="10" y1="10" x2="15" y2="15" stroke="#8a8a8a" stroke-width="2.4"/></svg>
      </span>
    </nav>

    <section class="slider" role="img" aria-label="Photo of medical researchers in lab coats examining a sample at a computer workstation">
      <div class="caption">
        <h2>Ullamcorper Ipsum Quam</h2>
        <p>Cras justo odio, dapibus ac facilisis in, egestas eget quam. Loremip. et, consectetur adipiscing elit. Fusce dapibus, tellus.</p>
      </div>
      <div class="slider-arrows">
        <svg width="9" height="6" viewBox="0 0 9 6"><path d="M9 3H1M3 1L1 3L3 5" fill="none" stroke="#fff"/></svg>
        <svg width="9" height="6" viewBox="0 0 9 6"><path d="M0 3H8M6 1L8 3L6 5" fill="none" stroke="#fff"/></svg>
      </div>
    </section>
    <div class="dots"><span></span><span></span><span class="active"></span></div>

    <h2 class="section-title">What we do?</h2>

    <div class="features">
      <div class="feature">
        <div class="feature-head">
          <span class="feature-icon"><svg width="17" height="17" viewBox="0 0 17 17"><circle cx="8.5" cy="8.5" r="6.5" fill="none" stroke="#fff" stroke-width="3"/><circle cx="8.5" cy="8.5" r="2.5" fill="#fff"/></svg></span>
          <h3>Online Q&amp;A</h3>
        </div>
        <p>Praesent commodo cursus magna, vel scelerisesq e nisl consectetur et. Donec ullamcorper nulla old n metus auctor fringilla Ipsum Etiam Condimentu.</p>
      </div>
      <div class="feature">
        <div class="feature-head">
          <span class="feature-icon"><svg width="17" height="17" viewBox="0 0 17 17"><circle cx="8.5" cy="8.5" r="7.5" fill="#fff"/><circle cx="8.5" cy="8.5" r="3" fill="#3d5d84"/></svg></span>
          <h3>Top Level Doctors</h3>
        </div>
        <p>Praesent commodo cursus magna, vel scelerisqss e nisl consectetur et. Donec ullamcorper nulla ose n metus auctor fringilla Ipsum Etiam Condimentu.</p>
      </div>
      <div class="feature">
        <div class="feature-head">
          <span class="feature-icon"><svg width="18" height="16" viewBox="0 0 18 16"><path d="M6 1L1 4L3 8L5 7V15H13V7L15 8L17 4L12 1C11 3 7 3 6 1Z" fill="#fff"/></svg></span>
          <h3>Clean Space</h3>
        </div>
        <p>Praesent commodo cursus magna, vel sceleriyuge e nisl consectetur et. Donec ullamcorper nulla nbr n metus auctor fringilla Ipsum Etiam Condimentu.</p>
      </div>
      <div class="feature">
        <div class="feature-head">
          <span class="feature-icon"><svg width="14" height="18" viewBox="0 0 14 18"><circle cx="7" cy="6.5" r="5.5" fill="#fff"/><rect x="4" y="11" width="6" height="3" fill="#fff"/><rect x="5" y="15" width="4" height="2" fill="#fff"/></svg></span>
          <h3>24 Hours Service</h3>
        </div>
        <p>Praesent commodo cursus magna, vel scelerisesq e nisl consectetur et. Donec ullamcorper nulla old n metus auctor fringilla Ipsum Etiam Condimentu.</p>
      </div>
      <div class="feature">
        <div class="feature-head">
          <span class="feature-icon"><svg width="18" height="18" viewBox="0 0 18 18"><rect x="5" y="-1" width="8" height="20" rx="4" transform="rotate(45 9 9)" fill="#fff"/><rect x="7" y="7" width="4" height="4" transform="rotate(45 9 9)" fill="#6b8db3"/></svg></span>
          <h3>Symptom Check</h3>
        </div>
        <p>Praesent commodo cursus magna, vel scelerisesq e nisl consectetur et. Donec ullamcorper nulla old n metus auctor fringilla Ipsum Etiam Condimentu.</p>
      </div>
      <div class="feature">
        <div class="feature-head">
          <span class="feature-icon"><svg width="20" height="12" viewBox="0 0 20 12"><rect x="0" y="1" width="20" height="10" rx="2" fill="#fff"/><line x1="10" y1="1" x2="10" y2="11" stroke="#3d5d84" stroke-width="1.5"/><line x1="3" y1="4" x2="8" y2="4" stroke="#3d5d84"/><line x1="3" y1="7" x2="8" y2="7" stroke="#3d5d84"/></svg></span>
          <h3>Dispense Medicine</h3>
        </div>
        <p>Praesent commodo cursus magna, vel scelerisesq e nisl consectetur et. Donec ullamcorper nulla nbr n metus auctor fringilla Ipsum Etiam Condimentu.</p>
      </div>
    </div>
  </main>
</body>
</html>
```